Print Ad Design

I need an ad designed to promote an event that we are hosting at a trade show for placement in the show program. The art must be ready to submit to the publication by Friday, November 15th at the latest. The ad is 1/2 page in the show program that will be 4.25"X 5.5" and must be submitted as a high resolution (300dpi) PDF. Ad is full colour. The minimum bleed and trim marks are 0.25". The trade show is the Northern Herd Fair in Canada and we would like to promote a 2 day training we will be hosting at the close of the show. Our company is PastureLink Systems - Ultrasound and Diagnostics and the details that should be included in the ad are:
YOU CAN USE ULTRASOUND TO MANAGE YOUR PREG CHECKS
On Farm Ultrasound Training for Producers
When - Friday, Feb. 7th & Saturday, Feb. 8th
9 AM - 5 PM
Where - close to Herd FAIR
Lunch provided
Registration $175 per day - $300 total
Introduction to ultrasound
Reproductive system anatomy
Pregnancy diagnosis
Live on farm scanning demonstrations and practice with case discussions
Tuition redeemable towards the purchase of ultrasound system.
TO REGISTER OR LEARN MORE
email - info@pasturelinksystems.ca or call 1-800-555-0147
(I have attached our logo and some possible images to use in the ad)
Please note that the primary logo to feature is PastureLink Systems and the secondary logo to use in the ad is Velorek Ultrasound Scanners.
THANK YOU!!!
Target Market(s)
Dairy Farmers (men and women)
Industry/Entity Type
Trade
Look and feel

```html
<!DOCTYPE html>
<html lang="en">
<head>
<meta charset="UTF-8">
<title>On Farm Ultrasound Training for Producers</title>
<link rel="stylesheet" href="https://fonts.googleapis.com/css2?family=Montserrat:wght@400;500;600;700&display=swap">
<style>
  :root {
    --yellow: #fdd22e;
    --yellow-soft: #ffe27a;
    --ink: #1c1c1c;
    --white: #ffffff;
    --navy: #1f4f8f;
    --sky: #2f86c8;
    --band-dark: #141414;
    --band-mid: #4a4a4a;
  }
  * { margin: 0; padding: 0; box-sizing: border-box; }
  html, body { width: 927px; height: 1200px; overflow: hidden; background: #ffffff; }
  body { font-family: "Montserrat", Arial, sans-serif; }
  .ad { position: relative; width: 927px; height: 1200px; overflow: hidden; }

  .hero-photo {
    position: absolute; left: 0; top: 0; width: 927px; height: 1030px;
    background:
      radial-gradient(ellipse at 30% 70%, rgba(120,120,120,.55), transparent 60%),
      radial-gradient(ellipse at 75% 35%, rgba(150,150,150,.35), transparent 55%),
      linear-gradient(180deg, #2b2b2b 0%, #3c3c3c 45%, #2a2a2a 100%);
  }

  .headline {
    position: absolute; left: 0; top: 62px; width: 927px; text-align: center;
    color: var(--yellow); font-weight: 500; font-size: 34px; line-height: 52px;
    letter-spacing: 0.5px;
  }
  .headline strong { font-weight: 700; }

  .event-title {
    position: absolute; left: 213px; top: 196px; color: var(--white);
    font-weight: 700; font-size: 49px; line-height: 57px;
  }
  .event-title .indent { display: block; padding-left: 164px; }

  .date-pill {
    position: absolute; left: 87px; top: 410px; width: 756px; height: 46px;
    background: var(--yellow); border-radius: 6px; color: var(--ink);
    font-weight: 700; font-size: 24px; line-height: 46px; text-align: center;
  }

  .venue-rule {
    position: absolute; left: 0; top: 470px; width: 927px; height: 32px;
    display: flex; align-items: center; color: var(--white);
    font-size: 24px; font-weight: 400;
  }
  .venue-rule::before, .venue-rule::after {
    content: ""; height: 2px; background: var(--white); flex: 1;
  }
  .venue-rule::before { flex: 0 0 462px; }
  .venue-rule span { padding: 0 12px; white-space: nowrap; }
  .venue-rule::after { flex: 0 0 36px; }
  .venue-rule strong { font-weight: 700; }

  .price-box {
    position: absolute; left: 159px; top: 522px; width: 606px; height: 86px;
    background: linear-gradient(180deg, var(--yellow) 0%, var(--yellow-soft) 100%);
    border-radius: 6px; color: var(--ink); text-align: center;
    padding-top: 6px;
  }
  .price-box .lunch { font-weight: 700; font-size: 25px; line-height: 36px; }
  .price-box .fee { font-weight: 400; font-size: 25px; line-height: 36px; }

  .topics {
    position: absolute; left: 216px; top: 622px; list-style: none;
    color: var(--white); font-weight: 700; font-size: 25px; line-height: 35px;
  }
  .topics li::before { content: "\2022\00a0"; }
  .topics .cont { display: block; padding-left: 27px; }

  .tuition-note {
    position: absolute; left: 60px; top: 837px; width: 802px; height: 51px;
    background: var(--yellow); border-radius: 4px 4px 0 0; color: var(--ink);
    font-weight: 700; font-size: 21px; line-height: 51px; text-align: center;
  }

  .contact-band {
    position: absolute; left: 0; top: 888px; width: 927px; height: 80px;
    background: linear-gradient(180deg, var(--band-mid) 0%, var(--band-dark) 100%);
    color: var(--white); text-align: center; padding-top: 9px;
  }
  .contact-band .cta { font-weight: 600; font-size: 22px; line-height: 30px; }
  .contact-band .details { font-weight: 400; font-size: 23px; line-height: 32px; }
  .contact-band strong { font-weight: 700; }

  .brand-strip {
    position: absolute; left: 0; top: 1030px; width: 927px; height: 137px;
    background: var(--white);
  }
  .primary-brand {
    position: absolute; left: 62px; top: 42px; display: flex; align-items: center; gap: 14px;
    color: var(--sky); font-weight: 700; font-size: 36px;
  }
  .primary-brand .dot { width: 42px; height: 42px; border-radius: 50%; background: var(--yellow); }
  .primary-brand .tag {
    position: absolute; left: 56px; top: 48px; white-space: nowrap;
    font-size: 17px; font-weight: 400; color: var(--sky);
  }
  .partner-brand {
    position: absolute; left: 520px; top: 38px; display: flex; align-items: center; gap: 12px;
    color: var(--navy); font-weight: 700; font-size: 22px; line-height: 28px;
  }
  .partner-brand .square { width: 30px; height: 30px; background: var(--yellow); }

  .foot-band {
    position: absolute; left: 0; top: 1167px; width: 927px; height: 33px;
    background: #2a2a2a;
  }
</style>
</head>
<body>
<main class="ad">
  <div class="hero-photo" role="img" aria-label="Photo of a producer wearing a gloved arm holding a portable ultrasound scanner during a pregnancy check on a dairy cow"></div>

  <h1 class="headline">YOU CAN USE <strong>ULTRASOUND</strong><br>TO MANAGE YOUR PREG CHECKS</h1>

  <h2 class="event-title">On Farm<br>Ultrasound Training<span class="indent">for Producers</span></h2>

  <p class="date-pill">Friday, Feb. 7th &amp; Saturday, Feb. 8th, 9 AM - 5 PM</p>

  <p class="venue-rule"><span>close to <strong>Herd FAIR</strong></span></p>

  <div class="price-box">
    <p class="lunch">Lunch provided</p>
    <p class="fee">Registration $175 per day - $300 total</p>
  </div>

  <ul class="topics">
    <li>Introduction to ultrasound</li>
    <li>Reproductive system anatomy</li>
    <li>Pregnancy diagnosis</li>
    <li>Live, on farm, scanning demonstrations<span class="cont">and practice with case discussions</span></li>
  </ul>

  <p class="tuition-note">Tuition redeemable towards the purchase of ultrasound system.</p>

  <div class="contact-band">
    <p class="cta">TO REGISTER OR LEARN MORE</p>
    <p class="details">email - <strong>info@pasturelinksystems.ca</strong> or call <strong>1-800-555-0147</strong></p>
  </div>

  <footer class="brand-strip">
    <div class="primary-brand">
      <span class="dot"></span>
      <span>PastureLink Systems</span>
      <span class="tag">ultrasound and diagnostics</span>
    </div>
    <div class="partner-brand">
      <span class="square"></span>
      <span>Velorek<br>Ultrasound Scanners</span>
    </div>
  </footer>
  <div class="foot-band"></div>
</main>
</body>
</html>
```